Mining Engineer Needs a Personal Design

Hi.

I would like a business card designed which includes a logo design. I would like it to be simple. Neat and tidy. I need this to go to print by Friday 1st August. The colours I would like you to use are black, royal blue and white. My initials TBH can be used to base this design on or my full name Troy Bell Hartley. The design should have one side with just the logo and one side with the logo and all my details below.

Troy Bell Hartley
Mining Engineer
M: +61 417 293 518
E: quarryhand@fernmail.example
Q: BEng (Mining Engineer), BComm (Management), RTQPA.

Industry/Entity Type

Business

```html
<!DOCTYPE html>
<html lang="en">
<head>
<meta charset="utf-8">
<title>Troy Bell Hartley – Business Card</title>
<link rel="stylesheet" href="https://fonts.googleapis.com/css2?family=Open+Sans:wght@400;600;800&display=swap">
<style>
  :root {
    --royal-blue: #1d5aa6;
    --ink: #1a1a1a;
    --paper: #f7f7f7;
    --white: #ffffff;
    --backdrop: #e4e4e2;
    --rule: #1d5aa6;
  }
  * { box-sizing: border-box; margin: 0; padding: 0; }
  html, body {
    width: 1200px; height: 757px; overflow: hidden;
    background: var(--backdrop);
    font-family: "Open Sans", Arial, sans-serif;
  }
  .sheet {
    position: relative; width: 1200px; height: 757px;
    display: flex; align-items: center; justify-content: center; gap: 60px;
  }
  .card {
    position: relative; width: 520px; height: 316px;
    box-shadow: 0 6px 18px rgba(0,0,0,0.18);
    overflow: hidden;
  }
  /* Front: logo only */
  .card-front {
    background: var(--royal-blue);
    display: flex; align-items: center; justify-content: center;
  }
  .monogram {
    font-weight: 800; letter-spacing: -1px; line-height: 1;
  }
  .card-front .monogram { color: var(--white); font-size: 64px; }

  /* Back: logo and details */
  .card-back { background: var(--paper); }
  .identity {
    position: absolute; left: 70px; top: 78px;
    display: flex; align-items: flex-end; gap: 10px;
  }
  .card-back .monogram { color: var(--royal-blue); font-size: 60px; }
  .qualifications {
    font-size: 11.5px; line-height: 1.25; color: var(--ink);
    padding-bottom: 6px; position: relative;
  }
  .qualifications .last {
    display: inline-block; padding-right: 60px;
    border-bottom: 1px solid var(--rule);
  }
  .person {
    position: absolute; left: 70px; top: 156px;
    display: flex; align-items: center; gap: 10px;
    color: var(--ink);
  }
  .person-name { font-size: 22px; font-weight: 400; }
  .divider { width: 1px; height: 18px; background: var(--royal-blue); }
  .person-role { font-size: 13px; }

  .contact-rule {
    position: absolute; left: 0; right: 0; bottom: 66px;
    height: 2px; background: var(--royal-blue);
  }
  .contact-band {
    position: absolute; left: 0; right: 0; bottom: 0; height: 60px;
    background: var(--royal-blue); color: var(--white);
    display: flex; align-items: center; justify-content: space-between;
    padding: 0 34px; font-size: 14px;
  }
  .contact-item { display: flex; align-items: center; gap: 12px; }
  .contact-item svg { width: 26px; height: 26px; flex: none; }
</style>
</head>
<body>
  <main class="sheet">
    <section class="card card-front" aria-label="Card front">
      <span class="monogram">TBH</span>
    </section>

    <section class="card card-back" aria-label="Card back">
      <div class="identity">
        <span class="monogram">TBH</span>
        <div class="qualifications">
          BEng (Mining Engineer)<br>
          BComm (Management)<br>
          <span class="last">RTQPA</span>
        </div>
      </div>

      <div class="person">
        <span class="person-name">Troy Bell Hartley</span>
        <span class="divider"></span>
        <span class="person-role">Mining Engineer</span>
      </div>

      <div class="contact-rule"></div>
      <div class="contact-band">
        <div class="contact-item">
          <svg viewBox="0 0 26 26" aria-hidden="true">
            <circle cx="13" cy="13" r="12" fill="none" stroke="#fff" stroke-width="1.2"/>
            <rect x="9.5" y="7" width="7" height="12" rx="1.2" fill="none" stroke="#fff" stroke-width="1.2"/>
            <line x1="12" y1="16.8" x2="14" y2="16.8" stroke="#fff" stroke-width="1.2"/>
          </svg>
          <span>+61 417 293 518</span>
        </div>
        <div class="contact-item">
          <svg viewBox="0 0 26 26" aria-hidden="true">
            <circle cx="13" cy="13" r="12" fill="none" stroke="#fff" stroke-width="1.2"/>
            <rect x="8" y="9" width="10" height="8" fill="#fff"/>
            <polyline points="8,9 13,13.5 18,9" fill="none" stroke="#1d5aa6" stroke-width="1"/>
          </svg>
          <span>quarryhand@fernmail.example</span>
        </div>
      </div>
    </section>
  </main>
</body>
</html>
```